Lift Every Ledger Through Chairside Trust

Design a cover for this book which is designed to help a business go from it's current revenue and treatment acceptance to double (2X) that success and those metrics.

```html
<!DOCTYPE html>
<html lang="en">
<head>
<meta charset="utf-8">
<title>Lift Every Ledger Through Chairside Trust — Book Cover</title>
<link rel="stylesheet" href="https://fonts.googleapis.com/css2?family=Bebas+Neue&family=Oswald:wght@500;700&display=swap">
<style>
  :root {
    --cover-blue: #0b86c9;
    --accent-yellow: #e2cc00;
    --title-white: #eef0f2;
    --cash-green: #8cc85a;
    --cash-green-dark: #4f9a34;
    --sleeve-navy: #2a3a9c;
  }
  * { margin: 0; padding: 0; box-sizing: border-box; }
  html, body {
    width: 953px;
    height: 1200px;
    overflow: hidden;
    background: var(--cover-blue);
  }
  .cover {
    position: relative;
    width: 953px;
    height: 1200px;
    background: var(--cover-blue);
    overflow: hidden;
  }
  .cover__spine-band {
    position: absolute;
    left: 0; top: 0;
    width: 18px; height: 100%;
    background: var(--accent-yellow);
  }
  .cover__frame-lines {
    position: absolute;
    inset: 0;
  }
  .cover__illustration {
    position: absolute;
    left: 600px;
    top: 140px;
    width: 240px;
    height: 580px;
    background: linear-gradient(170deg, var(--cash-green) 0%, var(--cash-green-dark) 55%, var(--sleeve-navy) 100%);
    border-radius: 10px;
    opacity: 0.9;
  }
  .title {
    position: absolute;
    left: 164px;
    top: 150px;
    font-family: "Bebas Neue", "Oswald", sans-serif;
    color: var(--title-white);
    line-height: 0.82;
  }
  .title__lead {
    display: block;
    font-size: 340px;
  }
  .title__main {
    display: block;
    font-size: 172px;
    margin-top: 34px;
  }
  .title__accent {
    display: block;
    font-size: 94px;
    color: var(--accent-yellow);
    margin-top: 40px;
    line-height: 0.95;
  }
  .author {
    position: absolute;
    left: 0;
    width: 953px;
    top: 1092px;
    text-align: center;
    font-family: "Oswald", sans-serif;
    font-weight: 500;
    font-size: 60px;
    letter-spacing: 0.14em;
    color: var(--title-white);
  }
</style>
</head>
<body>
  <main class="cover">
    <div class="cover__spine-band"></div>

    <svg class="cover__frame-lines" width="953" height="1200" viewBox="0 0 953 1200" aria-hidden="true">
      <g fill="none" stroke-width="8" stroke-linejoin="miter">
        <polyline points="27,134 111,64 648,64" stroke="var(--accent-yellow)"/>
        <polygon points="672,64 644,50 644,78" fill="var(--accent-yellow)" stroke="none"/>

        <polyline points="334,104 865,104 953,173" stroke="var(--title-white)"/>
        <polygon points="310,104 338,90 338,118" fill="var(--title-white)" stroke="none"/>

        <polyline points="10,902 97,975 648,975" stroke="var(--title-white)"/>
        <polygon points="672,975 644,961 644,989" fill="var(--title-white)" stroke="none"/>

        <polyline points="334,1006 865,1006 953,945" stroke="var(--accent-yellow)"/>
        <polygon points="310,1006 338,992 338,1020" fill="var(--accent-yellow)" stroke="none"/>
      </g>
    </svg>

    <div class="cover__illustration" role="img" aria-label="Illustration of a hand in a navy sleeve holding up two green dollar bills"></div>

    <h1 class="title">
      <span class="title__lead">Lift</span>
      <span class="title__main">Every Ledger</span>
      <span class="title__accent">Through Chairside Trust</span>
    </h1>

    <p class="author">WRITTER NAME</p>
  </main>
</body>
</html>
```